Create a Dynamic, Connecting, Professional looking PowerPoint Design master for our company.

Power point design

Target Market: High worth individuals and corporate group
Industry: Sport and services

Landscape format

Should include various slide such as:
Introduction page (photo background- inclusive logo)
Company presentation (with photos of various projects)
Different slide layouts to place general information with large photo & logo (in different sizes) as well as standard elements, such as text boxes, lines, default shapes, etc
Timeline page
Table pages
Various infographic style pages with editable chart
Our service page – Icons
Location page (world map)
Comparaison pages (3 offers to compare)
Closing page – thank you & contact
Page numbering

Colors:
#6ea6fa
#517ed8
#3758b4
#203390
#060d6c
#2EC193
White / Grey and black

Fonts:
Work sans / Helveticanow / Or other suitable.
Creative use of the logo in the slides. The Timrel icon may be used as a small device or large watermark to enhance branding.

The uploaded photos are indicative of the ones that we would like to use (ie: sail racing) there are here for you to include in the design but would need to be easily replaceable by the final photos we would be using.

If you have any questions or need any aditional material, please send me a message and I will try to respond to it as quickly as possible (bearing in mind that my time zone is UTC +2)

Target Market(s)

High worth individuals and corporate groups

Industry/Entity Type

Sport and services (sailing)

Font styles to use
Other font styles liked:
• Work Sans / Helveticanow

Colors
0054AA
0677BA
7BADD7
CADEEF
E8F1F8
00AB8E
00BBA5
67D7C9
C6EFE9
E9F9F6

Requirements
Must have
• Introduction page (photo background- inclusive logo) Company presentation (with photos of various projects) Different slide layouts to place general information with large photo & logo (in different sizes) as well as standard elements, such as text boxes, lines, default shapes, etc Timeline page Table pages Various infographic style pages with editable chart Our service page – Icons Location page (world map) Comparaison pages (3 offers to compare) Closing page – thank you & contact Page numbering
Nice to have
• Creative use of the logo in the slides. The Timrel icon may be used as a small device or large watermark to enhance branding.

```html
<!DOCTYPE html>
<html lang="en">
<head>
<meta charset="utf-8">
<title>Timrel – Presentation Master</title>
<link href="https://fonts.googleapis.com/css2?family=Poppins:ital,wght@0,300;0,400;0,500;0,600;0,700;1,700;1,800&display=swap" rel="stylesheet">
<style>
:root{
  --sky:#6ea6fa;--azure:#517ed8;--royal:#3758b4;--navy:#203390;--ink:#060d6c;--mint:#2ec193;
  --paper:#ffffff;--stage:#bdbdbd;--rule:#d4d4d4;--text:#1b1b2a;--muted:#8d8d99;--soft:#eef0f4;
}
*{box-sizing:border-box;margin:0;padding:0}
html,body{width:1200px;height:872px;overflow:hidden;background:var(--stage);font-family:"Poppins",sans-serif;color:var(--text)}
.deck{display:grid;grid-template-columns:repeat(4,286px);grid-auto-rows:161px;column-gap:10.5px;row-gap:7px;padding:20px 0 0 13px}
.slide{position:relative;background:var(--paper);overflow:hidden;box-shadow:0 1px 3px rgba(0,0,0,.25)}
.abs{position:absolute}
.slash{position:absolute;left:0;top:10px;width:20px;height:12px;background:var(--ink);clip-path:polygon(0 0,100% 0,55% 100%,0 100%)}
.slash::after{content:"";position:absolute;left:15px;top:0;width:6px;height:12px}
.slash-lite{position:absolute;left:16px;top:10px;width:9px;height:12px;background:var(--sky);clip-path:polygon(60% 0,100% 0,40% 100%,0 100%)}
.title{position:absolute;left:29px;top:10px;font-size:10.5px;font-weight:800;font-style:italic;color:var(--ink);letter-spacing:-.1px;white-space:nowrap}
.title em{color:var(--sky)}
.title.light{color:#fff}
.lede{position:absolute;left:120px;top:12px;width:110px;font-size:3.4px;line-height:1.3;color:#555}
.brand{position:absolute;right:20px;top:14px;display:flex;align-items:center;gap:1.5px;font-size:4.6px;font-weight:600;color:var(--ink);letter-spacing:.2px}
.brand::before{content:"";width:4px;height:4px;border-radius:50%;background:var(--ink)}
.brand.on-dark{color:#fff}.brand.on-dark::before{background:#fff}
.foot{position:absolute;left:0;right:0;bottom:0;height:2px;background:var(--rule)}
.corner{position:absolute;right:0;bottom:0;width:14px;height:9px;background:var(--sky);clip-path:polygon(60% 0,100% 0,100% 100%,0 100%)}
.pg{position:absolute;right:18px;bottom:4px;font-size:2.6px;color:var(--muted)}
.photo{position:absolute;background:linear-gradient(135deg,#5c6f8a,#22344f 60%,#2f6b5c)}
.photo.sea{background:linear-gradient(160deg,#8fa6b8,#2b4b63 55%,#1b3340)}
.photo.bright{background:linear-gradient(140deg,#c9d2d8,#5e7d92 50%,#3f8f64)}
.tiny{font-size:3px;line-height:1.35;color:#777}
.sub{font-size:4px;font-weight:600;color:var(--text)}
.para{position:relative}
.svc{position:absolute;width:118px;height:23px;clip-path:polygon(12% 0,100% 0,88% 100%,0 100%);color:#fff}
.svc b{position:absolute;left:32px;top:3px;font-size:4.6px;font-weight:500}
.svc p{position:absolute;left:32px;top:9px;width:70px;font-size:2.4px;line-height:1.3;opacity:.85}
.svc i{position:absolute;left:20px;top:8px;width:7px;height:6px;border:1px solid #fff;border-radius:1px}
.dot{position:absolute;border-radius:50%;display:flex;align-items:center;justify-content:center;color:#fff;font-size:4px;font-weight:500}
table{border-collapse:collapse}
.grid-tbl td,.grid-tbl th{font-weight:400}
.cal{position:absolute;left:17px;top:37px;width:252px}
.cal .mon{background:#4d5a78;color:#fff;text-align:center;font-size:4.4px;height:7px;line-height:7px}
.cal .days{display:grid;grid-template-columns:repeat(7,1fr);background:var(--soft);font-size:3px;text-align:center}
.cal .days span{height:9.3px;line-height:9.3px;color:#333}
.cal .days .hd{background:#d9dde5;height:7px;line-height:7px;color:#555}
.chart-bar{position:absolute;bottom:0}
.icon-c{position:absolute;width:14px;height:14px;border-radius:50%}
</style>
</head>
<body>
<main class="deck">

<!-- 1 Welcome -->
<section class="slide">
  <b class="brand" style="left:10px;right:auto;top:8px">TIMREL</b>
  <svg class="abs" style="left:0;top:0" width="286" height="161" viewBox="0 0 286 161">
    <polygon points="30,37 62,0 80,0 30,58" fill="none" stroke="#3758b4" stroke-width=".6"/>
    <polygon points="0,128 107,0 160,0 30,150" fill="#6ea6fa"/>
    <polygon points="45,161 175,0 178,0 48,161" fill="#2ec193"/>
    <polygon points="0,161 0,145 120,10 150,10 22,161" fill="#203390"/>
    <polygon points="0,161 35,161 150,28 122,28" fill="#060d6c" opacity=".85"/>
    <polygon points="248,30 286,30 286,75 223,112 213,112" fill="#3758b4"/>
    <polygon points="92,150 112,125 120,125 100,150" fill="#517ed8"/>
  </svg>
  <div class="photo sea" role="img" aria-label="Racing yacht heeling under full sail" style="left:95px;top:14px;width:190px;height:100px;clip-path:polygon(22% 0,100% 0,100% 40%,72% 100%,0 100%)"></div>
  <div class="abs" style="left:150px;top:116px;font-size:10px;font-weight:800;font-style:italic;color:var(--ink)">Welcome to our <span style="color:var(--sky)">race</span></div>
  <div class="abs" style="left:161px;top:131px;font-size:4.2px;color:#aaa">Place the sub heading text here</div>
</section>

<!-- 2 Company intro -->
<section class="slide">
  <i class="slash"></i><i class="slash-lite"></i>
  <h2 class="title">Company <em>Intro</em></h2>
  <p class="lede">Lorem ipsum dolor sit amet, consectetuer adipiscing elit. Maecenas porttitor congue massa.</p>
  <b class="brand">TIMREL</b>
  <div class="photo bright" role="img" aria-label="Catamarans racing past a hillside coast" style="left:17px;top:40px;width:251px;height:102px"></div>
  <div class="abs" style="left:17px;top:40px;width:95px;height:102px;background:rgba(32,51,144,.85);clip-path:polygon(0 0,100% 0,55% 100%,0 100%)"></div>
  <div class="abs" style="left:17px;top:40px;width:20px;height:20px;background:#fff;clip-path:polygon(0 0,100% 0,60% 100%,0 100%)"></div>
  <svg class="abs" style="left:21px;top:44px" width="9" height="9" viewBox="0 0 9 9"><path d="M1 8V1h6l-1.5 2L7 5H1" fill="none" stroke="#203390" stroke-width=".7"/></svg>
  <div class="abs" style="left:29px;top:82px;font-size:4.6px;font-weight:600;color:#fff;line-height:1.25">Layout with single<br>column and full <span style="color:var(--sky)">image</span></div>
  <p class="abs tiny" style="left:29px;top:98px;width:50px;color:#d8dcf2">Lorem ipsum is simply dummy text of the printing and typesetting industry.</p>
  <div class="foot"></div><i class="corner"></i><span class="pg">2</span>
</section>

<!-- 3 Company intro collage -->
<section class="slide">
  <i class="slash"></i><i class="slash-lite"></i>
  <h2 class="title">Company <em>Intro</em></h2>
  <p class="lede">Lorem ipsum dolor sit amet, consectetuer adipiscing elit. Maecenas porttitor congue massa.</p>
  <b class="brand">TIMREL</b>
  <svg class="abs" style="left:20px;top:42px" width="140" height="100" viewBox="0 0 140 100">
    <polygon points="65,0 75,0 68,10 58,10" fill="#6ea6fa"/>
    <polygon points="120,32 140,32 130,45 110,45" fill="#9aa0a8"/>
    <polygon points="108,35 125,35 105,62 88,62" fill="#203390"/>
    <polygon points="42,72 58,72 50,84 34,84" fill="#2ec193"/>
    <polygon points="82,72 98,72 90,84 74,84" fill="#6ea6fa"/>
  </svg>
  <div class="photo sea" role="img" aria-label="Collage of sailing project photos" style="left:30px;top:50px;width:110px;height:90px;clip-path:polygon(35% 0,70% 0,100% 30%,60% 100%,25% 100%,0 45%)"></div>
  <div class="abs sub" style="left:178px;top:70px;line-height:1.2">The New Experience<br>of <span style="color:var(--sky)">Adventure</span></div>
  <p class="abs tiny" style="left:178px;top:90px;width:75px">Lorem ipsum has been the industry's standard dummy text ever since the 1500s, when an unknown printer took a galley of type and scrambled it to make a type specimen book.</p>
  <div class="abs" style="left:178px;top:122px;width:30px;height:7px;background:var(--navy);clip-path:polygon(0 0,100% 0,85% 100%,0 100%);font-size:2.6px;color:#fff;line-height:7px;padding-left:4px">Read More</div>
  <div class="foot"></div><i class="corner"></i><span class="pg">3</span>
</section>

<!-- 4 Services with photo band -->
<section class="slide">
  <i class="slash"></i><i class="slash-lite"></i>
  <h2 class="title">Our <em>Services</em></h2>
  <p class="lede">Lorem ipsum dolor sit amet, consectetuer adipiscing elit. Maecenas porttitor congue massa.</p>
  <b class="brand">TIMREL</b>
  <div class="photo" role="img" aria-label="Trimaran bow slicing through water" style="left:0;top:28px;width:286px;height:122px;background:linear-gradient(120deg,#203390,#3758b4 45%,#2f8f86);clip-path:polygon(0 0,100% 0,100% 88%,0 100%)"></div>
  <div class="abs" style="left:28px;top:72px;width:100px;font-size:7.5px;color:#fff;line-height:1.15">Lorem ipsum <span style="color:var(--mint)">dolor sit amet</span>, consectetuer adipiscing elit.</div>
  <div class="abs" style="left:143px;top:48px;width:128px;display:grid;grid-template-columns:1fr 1fr;gap:3px">
    <div style="background:#fff;height:31px;padding:4px 3px"><div style="font-size:4.4px;text-align:right;color:#222">Our Services</div><p class="tiny" style="font-size:2.2px;margin-top:3px">Fusce posuere, magna sed pulvinar ultricies, purus lectus malesuada libero, sit amet.</p></div>
    <div style="background:#fff;height:31px;padding:4px 3px"><div style="font-size:4.4px;text-align:right;color:#222">Our Services</div><p class="tiny" style="font-size:2.2px;margin-top:3px">Fusce posuere, magna sed pulvinar ultricies, purus lectus malesuada libero, sit amet.</p></div>
    <div style="background:#fff;height:31px;padding:4px 3px"><div style="font-size:4.4px;text-align:right;color:#222">Our Services</div><p class="tiny" style="font-size:2.2px;margin-top:3px">Fusce posuere, magna sed pulvinar ultricies, purus lectus malesuada libero, sit amet.</p></div>
    <div style="background:#fff;height:31px;padding:4px 3px"><div style="font-size:4.4px;text-align:right;color:#222">Our Services</div><p class="tiny" style="font-size:2.2px;margin-top:3px">Fusce posuere, magna sed pulvinar ultricies, purus lectus malesuada libero, sit amet.</p></div>
  </div>
  <i class="corner"></i><span class="pg" style="color:#fff">4</span>
</section>

<!-- 5 Services icons -->
<section class="slide">
  <i class="slash"></i><i class="slash-lite"></i>
  <h2 class="title">Our <em>Services</em></h2>
  <p class="lede">Lorem ipsum dolor sit amet, consectetuer adipiscing elit. Maecenas porttitor congue massa.</p>
  <b class="brand">TIMREL</b>
  <div class="svc" style="left:20px;top:47px;background:var(--sky)"><i></i><b>Our Services</b><p>Fusce posuere, magna sed pulvinar ultricies, purus lectus malesuada libero.</p></div>
  <div class="svc" style="left:136px;top:47px;background:var(--navy)"><i></i><b>Our Services</b><p>Fusce posuere, magna sed pulvinar ultricies, purus lectus malesuada libero.</p></div>
  <div class="svc" style="left:20px;top:77px;background:var(--azure)"><i style="border-radius:50% 50% 0 0"></i><b>Our Services</b><p>Fusce posuere, magna sed pulvinar ultricies, purus lectus malesuada libero.</p></div>
  <div class="svc" style="left:136px;top:77px;background:var(--ink)"><i></i><b>Our Services</b><p>Fusce posuere, magna sed pulvinar ultricies, purus lectus malesuada libero.</p></div>
  <div class="svc" style="left:18px;top:107px;background:var(--royal)"><i></i><b>Our Services</b><p>Fusce posuere, magna sed pulvinar ultricies, purus lectus malesuada libero.</p></div>
  <div class="svc" style="left:134px;top:107px;background:var(--mint)"><i></i><b>Our Services</b><p>Fusce posuere, magna sed pulvinar ultricies, purus lectus malesuada libero.</p></div>
  <div class="foot"></div><i class="corner"></i><span class="pg">5</span>
</section>

<!-- 6 Project -->
<section class="slide">
  <i class="slash"></i><i class="slash-lite"></i>
  <h2 class="title">Our <em>Project</em></h2>
  <p class="lede">Lorem ipsum dolor sit amet, consectetuer adipiscing elit. Maecenas porttitor congue massa.</p>
  <b class="brand">TIMREL</b>
  <div class="photo bright" role="img" aria-label="Five project photos of crews and yachts" style="left:20px;top:47px;width:250px;height:48px;clip-path:polygon(8% 0,100% 0,92% 100%,0 100%)"></div>
  <svg class="abs" style="left:20px;top:47px" width="250" height="48"><g stroke="#fff" stroke-width="3"><line x1="60" y1="0" x2="40" y2="48"/><line x1="104" y1="0" x2="84" y2="48"/><line x1="148" y1="0" x2="128" y2="48"/><line x1="192" y1="0" x2="172" y2="48"/></g></svg>
  <div class="abs" style="left:22px;top:90px;width:250px;display:grid;grid-template-columns:repeat(5,44.5px);font-size:4px">
    <div><div style="background:#fff;width:16px;text-align:center;color:#555">01</div><div class="sub" style="margin-top:3px;font-size:3.6px">Your subtitle here</div><p class="tiny" style="margin-top:3px;width:32px">Lorem ipsum is simply dummy text of the printing and typesetting.</p></div>
    <div><div style="background:#fff;width:16px;text-align:center;color:#555">02</div><div class="sub" style="margin-top:3px;font-size:3.6px">Your subtitle here</div><p class="tiny" style="margin-top:3px;width:32px">Lorem ipsum is simply dummy text of the printing and typesetting.</p></div>
    <div><div style="background:#fff;width:16px;text-align:center;color:#555">03</div><div class="sub" style="margin-top:3px;font-size:3.6px">Your subtitle here</div><p class="tiny" style="margin-top:3px;width:32px">Lorem ipsum is simply dummy text of the printing and typesetting.</p></div>
    <div><div style="background:#fff;width:16px;text-align:center;color:#555">04</div><div class="sub" style="margin-top:3px;font-size:3.6px">Your subtitle here</div><p class="tiny" style="margin-top:3px;width:32px">Lorem ipsum is simply dummy text of the printing and typesetting.</p></div>
    <div><div style="background:#fff;width:16px;text-align:center;color:#555">05</div><div class="sub" style="margin-top:3px;font-size:3.6px">Your subtitle here</div><p class="tiny" style="margin-top:3px;width:32px">Lorem ipsum is simply dummy text of the printing and typesetting.</p></div>
  </div>
  <div class="foot"></div><i class="corner"></i><span class="pg">6</span>
</section>

<!-- 7 Timeline -->
<section class="slide">
  <i class="slash"></i><i class="slash-lite"></i>
  <h2 class="title">Our <em>Timeline</em></h2>
  <p class="lede">Lorem ipsum dolor sit amet, consectetuer adipiscing elit. Maecenas porttitor congue massa.</p>
  <b class="brand">TIMREL</b>
  <svg class="abs" style="left:0;top:54px" width="286" height="90">
    <polygon points="0,0 255,0 251,6 0,6" fill="#6ea6fa"/><polygon points="130,0 255,0 251,6 126,6" fill="#203390"/>
    <g stroke="#6ea6fa" stroke-width=".5"><line x1="91" y1="6" x2="91" y2="23"/><line x1="127" y1="6" x2="127" y2="50"/><line x1="176" y1="6" x2="176" y2="19"/><line x1="254" y1="6" x2="254" y2="70"/></g>
  </svg>
  <div class="dot" style="left:81px;top:77px;width:20px;height:20px;background:var(--azure)">2015</div>
  <div class="dot" style="left:117px;top:104px;width:20px;height:20px;background:var(--royal)">2017</div>
  <div class="dot" style="left:166px;top:73px;width:20px;height:20px;background:var(--navy)">2020</div>
  <div class="dot" style="left:244px;top:124px;width:20px;height:20px;background:var(--sky)">2022</div>
  <div class="abs" style="left:25px;top:79px;width:53px;text-align:right"><div class="sub" style="font-size:3.8px">Your subtitle here</div><p class="tiny">Lorem ipsum is simply dummy text of the printing and typesetting.</p></div>
  <div class="abs" style="left:141px;top:103px;width:53px"><div class="sub" style="font-size:3.8px">Your subtitle here</div><p class="tiny">Lorem ipsum is simply dummy text of the printing and typesetting.</p></div>
  <div class="abs" style="left:191px;top:71px;width:53px"><div class="sub" style="font-size:3.8px">Your subtitle here</div><p class="tiny">Lorem ipsum is simply dummy text of the printing and typesetting.</p></div>
  <div class="abs" style="left:188px;top:128px;width:53px;text-align:right"><div class="sub" style="font-size:3.8px">Your subtitle here</div><p class="tiny">Lorem ipsum is simply dummy text of the printing and typesetting.</p></div>
  <div class="foot"></div><i class="corner"></i><span class="pg">7</span>
</section>

<!-- 8 Milestone -->
<section class="slide">
  <i class="slash"></i><i class="slash-lite"></i>
  <h2 class="title">Our <em>Milestone</em></h2>
  <p class="lede">Lorem ipsum dolor sit amet, consectetuer adipiscing elit. Maecenas porttitor congue massa.</p>
  <b class="brand">TIMREL</b>
  <svg class="abs" style="left:0;top:0" width="286" height="161">
    <line x1="14" y1="130" x2="265" y2="130" stroke="#3758b4" stroke-width=".5" stroke-dasharray="1.5 1.5"/>
    <g stroke-width="1.2"><line x1="54" y1="93" x2="54" y2="130" stroke="#6ea6fa"/><line x1="97" y1="75" x2="97" y2="130" stroke="#517ed8"/><line x1="138" y1="93" x2="138" y2="130" stroke="#3758b4"/><line x1="180" y1="75" x2="180" y2="130" stroke="#060d6c"/><line x1="222" y1="93" x2="222" y2="130" stroke="#2ec193"/></g>
    <g fill="#fff" stroke-width="1.2"><circle cx="54" cy="130" r="2.5" stroke="#6ea6fa"/><circle cx="97" cy="130" r="2.5" stroke="#517ed8"/><circle cx="138" cy="130" r="2.5" stroke="#3758b4"/><circle cx="180" cy="130" r="2.5" stroke="#060d6c"/><circle cx="222" cy="130" r="2.5" stroke="#2ec193"/></g>
  </svg>
  <div class="dot" style="left:42px;top:78px;width:24px;height:24px;background:var(--sky)">2015</div>
  <div class="dot" style="left:85px;top:57px;width:24px;height:24px;background:var(--azure)">2017</div>
  <div class="dot" style="left:126px;top:78px;width:24px;height:24px;background:var(--royal)">2019</div>
  <div class="dot" style="left:168px;top:57px;width:24px;height:24px;background:var(--ink)">2021</div>
  <div class="dot" style="left:210px;top:78px;width:24px;height:24px;background:var(--mint)">2023</div>
  <div class="abs tiny" style="left:60px;top:107px;width:24px;font-size:3.8px">Write your paragraph here</div>
  <div class="abs tiny" style="left:103px;top:107px;width:24px;font-size:3.8px">Write your paragraph here</div>
  <div class="abs tiny" style="left:144px;top:107px;width:24px;font-size:3.8px">Write your paragraph here</div>
  <div class="abs tiny" style="left:186px;top:107px;width:24px;font-size:3.8px">Write your paragraph here</div>
  <div class="abs tiny" style="left:228px;top:107px;width:24px;font-size:3.8px">Write your paragraph here</div>
  <div class="foot"></div><i class="corner"></i><span class="pg">8</span>
</section>

<!-- 9 Table layout -->
<section class="slide" style="background:linear-gradient(160deg,#243a4a,#0f2a3b 45%,#122a6a)">
  <div class="abs" role="img" aria-label="Dark sea and sail background" style="inset:0;background:linear-gradient(180deg,rgba(46,193,147,.25),rgba(6,13,108,.55))"></div>
  <h2 class="title light" style="left:22px;top:12px">Table <em>Layout</em></h2>
  <p class="lede" style="left:133px;width:110px;color:#dde">Lorem ipsum dolor sit amet, consectetuer adipiscing elit. Maecenas porttitor congue massa.</p>
  <table class="abs grid-tbl" style="left:22px;top:50px;width:248px;font-size:3.4px;color:#e6e9f5">
    <tr style="height:8px;color:#fff"><th style="width:88px"></th><th style="background:var(--sky)">Label 1</th><th style="background:var(--azure)">Label 2</th><th style="background:var(--royal)">Label 3</th><th style="background:var(--mint)">Label 4</th></tr>
    <tr style="height:9.8px;border-bottom:.5px solid rgba(255,255,255,.3)"><td>Lorem ipsum is simply dummy text</td><td align="center" style="color:var(--mint)">●</td><td align="center">✕</td><td align="center" style="color:var(--mint)">●</td><td align="center" style="color:var(--mint)">●</td></tr>
    <tr style="height:9.8px;border-bottom:.5px solid rgba(255,255,255,.3)"><td>It has roots in a piece of.</td><td align="center">✕</td><td align="center">✕</td><td align="center" style="color:var(--mint)">●</td><td align="center">✕</td></tr>
    <tr style="height:9.8px;border-bottom:.5px solid rgba(255,255,255,.3)"><td>Lorem ipsum is not simply random text.</td><td align="center" style="color:var(--mint)">●</td><td align="center" style="color:var(--mint)">●</td><td align="center">✕</td><td align="center">✕</td></tr>
    <tr style="height:9.8px;border-bottom:.5px solid rgba(255,255,255,.3)"><td>Lorem ipsum is simply dummy text</td><td align="center" style="color:var(--mint)">●</td><td align="center" style="color:var(--mint)">●</td><td align="center" style="color:var(--mint)">●</td><td align="center">✕</td></tr>
    <tr style="height:9.8px;border-bottom:.5px solid rgba(255,255,255,.3)"><td>It has roots in a piece of.</td><td align="center" style="color:var(--mint)">●</td><td align="center" style="color:var(--mint)">●</td><td align="center">✕</td><td align="center" style="color:var(--mint)">●</td></tr>
    <tr style="height:9.8px;border-bottom:.5px solid rgba(255,255,255,.3)"><td>Lorem ipsum is not simply random text.</td><td align="center">✕</td><td align="center" style="color:var(--mint)">●</td><td align="center">✕</td><td align="center" style="color:var(--mint)">●</td></tr>
    <tr style="height:9.8px;border-bottom:.5px solid rgba(255,255,255,.3)"><td>Lorem ipsum is simply dummy text</td><td align="center">✕</td><td align="center" style="color:var(--mint)">●</td><td align="center" style="color:var(--mint)">●</td><td align="center">✕</td></tr>
    <tr style="height:9.8px;border-bottom:.5px solid rgba(255,255,255,.3)"><td>It has roots in a piece of.</td><td align="center">✕</td><td align="center" style="color:var(--mint)">●</td><td align="center" style="color:var(--mint)">●</td><td align="center">✕</td></tr>
    <tr style="height:10px"><td></td><td align="center">$ 99,99</td><td align="center">$ 99,99</td><td align="center">$ 99,99</td><td align="center">$ 99,99</td></tr>
  </table>
</section>

<!-- 10 Annual table -->
<section class="slide">
  <i class="slash"></i><i class="slash-lite"></i>
  <h2 class="title">Annual <em>Table</em></h2>
  <p class="lede">Lorem ipsum dolor sit amet, consectetuer adipiscing elit. Maecenas porttitor congue massa.</p>
  <b class="brand">TIMREL</b>
  <div class="abs" style="left:20px;top:41px;width:22px;height:22px;border:1.2px solid var(--ink);border-radius:50%"></div>
  <div class="abs" style="left:53px;top:41px;width:22px;height:22px;border:1.2px solid var(--ink);border-radius:50%"></div>
  <svg class="abs" style="left:20px;top:41px" width="56" height="22"><g stroke="#060d6c" stroke-width="1.2" stroke-linecap="round"><line x1="6" y1="6" x2="16" y2="16"/><line x1="16" y1="6" x2="6" y2="16"/><line x1="44" y1="5" x2="44" y2="17"/></g></svg>
  <div class="abs sub" style="left:85px;top:43px;font-size:4.4px">Company budget files 2021</div>
  <p class="abs tiny" style="left:85px;top:50px;width:136px;font-style:italic;font-size:2.6px">Lorem ipsum dolor sit amet, ligula suspendisse nulla pretium, rhoncus tempor fermentum, enim integer ad vestibulum volutpat. Nisl rhoncus turpis est, vel elit, congue wisi enim nunc ultricies sit, magna tincidunt.</p>
  <table class="abs" style="left:20px;top:69px;width:202px;font-size:3.6px;color:#999">
    <tr style="color:var(--azure);height:7px;border-bottom:.5px solid #ccc"><td>Nisl rhoncus turpis est</td><td>2014</td><td>2015</td><td>2016</td><td>2017</td></tr>
    <tr style="height:12px;border-bottom:.5px solid #ddd"><td>Praesent condimentum arcu</td><td>4.456</td><td>4.456</td><td>4.456</td><td>4.456</td></tr>
    <tr style="height:12px;border-bottom:.5px solid #ddd"><td>Praesent condimentum arcu</td><td>5.345</td><td>5.345</td><td>5.345</td><td>5.345</td></tr>
    <tr style="height:12px;border-bottom:.5px solid #ddd"><td>Praesent condimentum arcu</td><td>6.567</td><td>6.567</td><td>6.567</td><td>6.567</td></tr>
    <tr style="height:12px;border-bottom:.5px solid #ddd"><td>Praesent condimentum arcu</td><td>7.678</td><td>7.678</td><td>7.678</td><td>7.678</td></tr>
    <tr style="height:12px;border-bottom:.5px solid #ddd"><td>Praesent condimentum arcu</td><td>8.789</td><td>8.789</td><td>8.789</td><td>8.789</td></tr>
    <tr style="height:7px;color:#333"><td>CHANGE 20%</td><td></td><td></td><td></td><td></td></tr>
  </table>
  <div class="abs" style="left:224px;top:40px;width:62px;height:113px;background:var(--azure);color:#dfe8ff;font-size:3.8px">
    <div style="background:#4d5a78;height:12px;line-height:12px;padding-left:7px;color:#fff">STATS MANAGER</div>
    <div style="padding:5px 14px;height:25px;border-bottom:.6px solid #fff">THIS YEAR<br><span style="color:#fff;font-size:4.4px">17,250</span></div>
    <div style="padding:5px 14px;height:25px;border-bottom:.6px solid #fff">THIS MONTH<br><span style="color:#fff;font-size:4.4px">3,000</span></div>
    <div style="padding:5px 14px;height:25px;border-bottom:.6px solid #fff">THIS WEEK<br><span style="color:#fff;font-size:4.4px">450</span></div>
    <div style="padding:5px 14px">TODAY<br><span style="color:#fff;font-size:4.4px">225</span></div>
  </div>
  <div class="foot"></div><i class="corner"></i><span class="pg" style="right:70px">10</span>
</section>

<!-- 11 Calendar -->
<section class="slide">
  <i class="slash"></i><i class="slash-lite"></i>
  <h2 class="title">Calendar <em>Table</em></h2>
  <p class="lede">Lorem ipsum dolor sit amet, consectetuer adipiscing elit. Maecenas porttitor congue massa.</p>
  <b class="brand">TIMREL</b>
  <div class="cal">
    <div class="mon">July</div>
    <div class="days">
      <span class="hd">Sun</span><span class="hd">Mon</span><span class="hd">Tue</span><span class="hd">Wed</span><span class="hd">Thu</span><span class="hd">Fri</span><span class="hd">Sat</span>
      <span></span><span></span><span>1</span><span>2</span><span>3</span><span>4</span><span>5</span>
      <span>6</span><span>7</span><span style="background:var(--azure);color:#fff">8</span><span>9</span><span>10</span><span>11</span><span style="background:var(--ink);color:#fff">12</span>
      <span>13</span><span>14</span><span>15</span><span>16</span><span>17</span><span>18</span><span>19</span>
      <span>20</span><span>21</span><span>22</span><span>23</span><span>24</span><span>25</span><span>26</span>
      <span>27</span><span>28</span><span>29</span><span style="background:var(--mint);color:#fff">30</span><span>31</span><span></span><span></span>
    </div>
  </div>
  <div class="icon-c" style="left:19px;top:112px;background:var(--azure)"></div>
  <div class="icon-c" style="left:103px;top:112px;background:var(--mint)"></div>
  <div class="icon-c" style="left:186px;top:112px;background:var(--ink)"></div>
  <div class="abs" style="left:40px;top:113px;width:60px"><div class="sub" style="font-size:4px">Knowledge</div><p class="tiny" style="margin-top:2px">To get your company's name out there, you need to make sure.</p></div>
  <div class="abs" style="left:124px;top:113px;width:60px"><div class="sub" style="font-size:4px">Awareness</div><p class="tiny" style="margin-top:2px">To get your company's name out there, you need to make sure.</p></div>
  <div class="abs" style="left:207px;top:113px;width:60px"><div class="sub" style="font-size:4px">Reinforcement</div><p class="tiny" style="margin-top:2px">To get your company's name out there, you need to make sure.</p></div>
  <div class="foot"></div><i class="corner"></i><span class="pg">11</span>
</section>

<!-- 12 Product image cards -->
<section class="slide">
  <i class="slash"></i><i class="slash-lite"></i>
  <h2 class="title">Product <em>Image</em></h2>
  <p class="lede">Lorem ipsum dolor sit amet, consectetuer adipiscing elit. Maecenas porttitor congue massa.</p>
  <b class="brand">TIMREL</b>
  <div class="abs" style="left:26px;top:40px;width:55px;height:101px;background:var(--soft)"></div>
  <div class="abs" style="left:99px;top:40px;width:55px;height:101px;background:var(--soft)"></div>
  <div class="abs" style="left:172px;top:40px;width:55px;height:101px;background:var(--soft)"></div>
  <div class="photo sea" role="img" aria-label="Yacht sails close up" style="left:26px;top:40px;width:55px;height:58px;clip-path:polygon(0 0,100% 0,100% 55%,72% 100%,0 100%)"></div>
  <div class="photo bright" role="img" aria-label="Green hulled racer at speed" style="left:99px;top:40px;width:55px;height:58px;clip-path:polygon(0 0,100% 0,100% 55%,72% 100%,0 100%)"></div>
  <div class="photo sea" role="img" aria-label="Racing yacht with spinnaker" style="left:172px;top:40px;width:55px;height:58px;clip-path:polygon(0 0,100% 0,100% 55%,72% 100%,0 100%)"></div>
  <div class="abs" style="left:26px;top:83px;width:35px;height:9px;background:var(--ink);color:#fff;font-size:4.4px;padding-left:4px;line-height:9px">SKU01</div>
  <div class="abs" style="left:26px;top:92px;width:16px;height:6px;background:var(--ink);color:#fff;font-size:3px;padding-left:3px;line-height:6px">$10.5</div>
  <div class="abs" style="left:99px;top:83px;width:35px;height:9px;background:var(--sky);color:#fff;font-size:4.4px;padding-left:4px;line-height:9px">SKU02</div>
  <div class="abs" style="left:99px;top:92px;width:16px;height:6px;background:var(--sky);color:#fff;font-size:3px;padding-left:3px;line-height:6px">$10.5</div>
  <div class="abs" style="left:172px;top:83px;width:35px;height:9px;background:var(--mint);color:#fff;font-size:4.4px;padding-left:4px;line-height:9px">SKU03</div>
  <div class="abs" style="left:172px;top:92px;width:16px;height:6px;background:var(--mint);color:#fff;font-size:3px;padding-left:3px;line-height:6px">$10.5</div>
  <div class="abs" style="left:30px;top:104px;width:48px"><div class="sub" style="font-size:3.8px">Product Description</div><p class="tiny" style="margin-top:2px">Lorem ipsum is simply dummy text of the printing and typesetting industry.</p></div>
  <div class="abs" style="left:103px;top:104px;width:48px"><div class="sub" style="font-size:3.8px">Product Description</div><p class="tiny" style="margin-top:2px">Lorem ipsum is simply dummy text of the printing and typesetting industry.</p></div>
  <div class="abs" style="left:176px;top:104px;width:48px"><div class="sub" style="font-size:3.8px">Product Description</div><p class="tiny" style="margin-top:2px">Lorem ipsum is simply dummy text of the printing and typesetting industry.</p></div>
  <div class="foot"></div><i class="corner"></i><span class="pg">12</span>
</section>

<!-- 13 Product image drawing -->
<section class="slide">
  <i class="slash"></i><i class="slash-lite"></i>
  <h2 class="title">Product <em>Image</em></h2>
  <p class="lede">Lorem ipsum dolor sit amet, consectetuer adipiscing elit. Maecenas porttitor congue massa.</p>
  <b class="brand">TIMREL</b>
  <div class="abs" style="left:25px;top:44px;width:63px;height:92px;background:#4d5a78;color:#fff;padding:7px 7px">
    <div style="font-size:4.6px;line-height:1.2">Lorem Ipsum is simply dummy text</div>
    <p style="font-size:2.6px;line-height:1.35;opacity:.8;margin-top:4px">It has roots in a piece of classical Latin literature from 45 BC, making it over 2000 years old.</p>
    <div style="font-size:2.8px;margin-top:6px;border-bottom:1px solid var(--sky);padding-bottom:2px">Product Features</div>
    <div style="font-size:2.8px;margin-top:4px;border-bottom:1px solid var(--sky);padding-bottom:2px">Product Features</div>
    <div style="font-size:2.8px;margin-top:4px;border-bottom:1px solid var(--sky);padding-bottom:2px">Product Features</div>
  </div>
  <div class="abs" style="left:74px;top:122px;width:14px;height:14px;background:var(--sky);clip-path:polygon(100% 0,100% 100%,0 100%)"></div>
  <div class="abs" style="left:93px;top:44px;width:40px;height:9px;background:var(--ink);color:#fff;font-size:4.4px;padding-left:4px;line-height:9px;clip-path:polygon(0 0,100% 0,88% 100%,0 100%)">SKU01</div>
  <div class="abs" style="left:93px;top:54px;width:22px;height:7px;background:var(--ink);color:#fff;font-size:3px;padding-left:3px;line-height:7px;clip-path:polygon(0 0,100% 0,80% 100%,0 100%)">$10.5</div>
  <div class="abs" role="img" aria-label="Technical side and deck plan drawing of the yacht" style="left:118px;top:50px;width:150px;height:80px;background:linear-gradient(180deg,#f4f5f8,#e6e8ee)"></div>
  <div class="foot"></div><i class="corner"></i><span class="pg">13</span>
</section>

<!-- 14 Section break -->
<section class="slide">
  <svg class="abs" style="left:0;top:0" width="286" height="161"><polygon points="208,0 286,0 286,161 83,161" fill="#060d6c"/><polygon points="180,60 210,20 220,20 190,60" fill="#517ed8"/></svg>
  <div class="abs" style="left:17px;top:25px;width:90px;height:90px;border-radius:50%;background:radial-gradient(circle,#f6f7fa,#fff 70%)"></div>
  <div class="photo bright" role="img" aria-label="Green hulled yacht racing in open water" style="left:145px;top:27px;width:141px;height:106px;clip-path:polygon(40% 0,100% 0,100% 100%,0 100%)"></div>
  <div class="abs" style="left:210px;top:6px;width:100px;height:18px;background:var(--royal);clip-path:polygon(25% 0,100% 0,100% 100%,0 100%)"></div>
  <b class="brand on-dark" style="top:10px">TIMREL</b>
  <div class="abs" style="left:126px;top:107px;width:44px;height:10px;background:var(--sky);color:#fff;font-size:4px;line-height:10px;padding-left:8px;clip-path:polygon(15% 0,100% 0,85% 100%,0 100%)">10.00 – 10.15</div>
  <div class="abs" style="left:23px;top:67px;font-size:10px;font-weight:800;font-style:italic;color:var(--ink)">Section <span style="color:var(--sky)">Break</span></div>
  <div class="abs" style="left:23px;top:81px;font-size:4.4px;color:#666">Place the sub heading text here</div>
  <div class="abs" style="left:249px;top:143px;display:flex;gap:1px"><i style="width:6px;height:6px;border:.5px solid var(--sky)"></i><i style="width:6px;height:6px;border:.5px solid var(--sky)"></i><i style="width:6px;height:6px;border:.5px solid var(--sky)"></i><i style="width:6px;height:6px;border:.5px solid var(--sky)"></i></div>
</section>

<!-- 15 Graph chart bars -->
<section class="slide">
  <i class="slash"></i><i class="slash-lite"></i>
  <h2 class="title">Graph <em>Chart</em></h2>
  <p class="lede">Lorem ipsum dolor sit amet, consectetuer adipiscing elit. Maecenas porttitor congue massa.</p>
  <b class="brand">TIMREL</b>
  <svg class="abs" style="left:25px;top:45px" width="140" height="95" viewBox="0 0 140 95" font-size="3.4" fill="#888" font-family="Poppins,sans-serif">
    <g stroke="#bbb" stroke-width=".4" stroke-dasharray="1 1"><line x1="14" y1="0" x2="14" y2="50"/><line x1="32" y1="0" x2="32" y2="70"/><line x1="50" y1="0" x2="50" y2="50"/><line x1="68" y1="0" x2="68" y2="45"/><line x1="86" y1="0" x2="86" y2="60"/><line x1="104" y1="0" x2="104" y2="30"/><line x1="122" y1="0" x2="122" y2="20"/></g>
    <g fill="#bdbdbd"><rect x="10" y="50" width="9" height="32"/><rect x="28" y="70" width="9" height="12"/><rect x="46" y="50" width="9" height="32"/><rect x="64" y="45" width="9" height="37"/><rect x="82" y="60" width="9" height="22"/><rect x="100" y="30" width="9" height="52"/><rect x="118" y="20" width="9" height="62"/></g>
    <rect x="136" y="5" width="9" height="77" fill="#6ea6fa"/>
    <g text-anchor="middle"><text x="14" y="89">2010</text><text x="32" y="89">2011</text><text x="50" y="89">2012</text><text x="68" y="89">2013</text><text x="86" y="89">2014</text><text x="104" y="89">2015</text><text x="122" y="89">2016</text><text x="140" y="89">2017</text></g>
  </svg>
  <svg class="abs" style="left:200px;top:43px" width="11" height="11"><circle cx="5.5" cy="5.5" r="4.5" fill="none" stroke="#203390" stroke-width=".6"/><path d="M3.3 5.6l1.6 1.6 3-3.2" fill="none" stroke="#203390" stroke-width=".6"/></svg>
  <div class="abs" style="left:180px;top:56px;width:50px;text-align:center"><div style="font-size:6px;font-weight:600;color:var(--ink)">we are <span style="color:var(--sky)">growing</span></div><p class="tiny" style="margin-top:2px">lorem ipsum dolor sit amet, consectetuer adipiscing elit. maecenas</p></div>
  <svg class="abs" style="left:200px;top:91px" width="11" height="11"><circle cx="5.5" cy="5.5" r="4.5" fill="none" stroke="#203390" stroke-width=".6"/><path d="M5.5 3v5M3 5.5h5" stroke="#203390" stroke-width=".6"/></svg>
  <div class="abs" style="left:180px;top:104px;width:50px;text-align:center"><div style="font-size:6px;font-weight:600;color:var(--ink)"><span style="color:var(--sky)">join</span> the crew</div><p class="tiny" style="margin-top:2px">lorem ipsum dolor sit amet, consectetuer adipiscing elit. maecenas</p></div>
  <div class="foot"></div><i class="corner"></i><span class="pg">15</span>
</section>

<!-- 16 Graph chart grouped -->
<section class="slide">
  <i class="slash"></i><i class="slash-lite"></i>
  <h2 class="title">Graph <em>Chart</em></h2>
  <p class="lede">Lorem ipsum dolor sit amet, consectetuer adipiscing elit. Maecenas porttitor congue massa.</p>
  <b class="brand">TIMREL</b>
  <svg class="abs" style="left:18px;top:36px" width="155" height="110" viewBox="0 0 155 110" font-size="3.6" fill="#888" font-family="Poppins,sans-serif">
    <g stroke="#e2e2e2" stroke-width=".4"><line x1="10" y1="5" x2="155" y2="5"/><line x1="10" y1="18.5" x2="155" y2="18.5"/><line x1="10" y1="32" x2="155" y2="32"/><line x1="10" y1="45.5" x2="155" y2="45.5"/><line x1="10" y1="59" x2="155" y2="59"/><line x1="10" y1="72.5" x2="155" y2="72.5"/><line x1="10" y1="86" x2="155" y2="86"/></g>
    <g><text x="2" y="7">6</text><text x="2" y="20">5</text><text x="2" y="34">4</text><text x="2" y="47">3</text><text x="2" y="61">2</text><text x="2" y="74">1</text><text x="2" y="88">0</text></g>
    <rect x="26" y="28" width="7.5" height="58" fill="#203390"/><rect x="34" y="52" width="7.5" height="34" fill="#777"/><rect x="42" y="25" width="7.5" height="61" fill="#6ea6fa"/>
    <rect x="72" y="18.5" width="7.5" height="67.5" fill="#203390"/><rect x="80" y="39" width="7.5" height="47" fill="#777"/><rect x="88" y="45.5" width="7.5" height="40.5" fill="#6ea6fa"/>
    <rect x="118" y="53" width="7.5" height="33" fill="#203390"/><rect x="126" y="27" width="7.5" height="59" fill="#777"/><rect x="134" y="48" width="7.5" height="38" fill="#6ea6fa"/>
    <g text-anchor="middle"><text x="38" y="95">category 1</text><text x="84" y="95">category 2</text><text x="130" y="95">category 3</text></g>
  </svg>
  <div class="icon-c" style="left:176px;top:47px;width:12px;height:12px;background:var(--navy)"></div>
  <div class="icon-c" style="left:176px;top:78px;width:12px;height:12px;background:#777"></div>
  <div class="icon-c" style="left:176px;top:109px;width:12px;height:12px;background:var(--sky)"></div>
  <div class="abs" style="left:198px;top:47px;width:60px"><div style="font-size:4.6px;font-weight:600">option one</div><p class="tiny" style="margin-top:1px">Lorem ipsum dolor sit amet, consectetuer adipiscing elit.</p></div>
  <div class="abs" style="left:198px;top:78px;width:60px"><div style="font-size:4.6px;font-weight:600">option two</div><p class="tiny" style="margin-top:1px">Lorem ipsum dolor sit amet, consectetuer adipiscing elit.</p></div>
  <div class="abs" style="left:198px;top:109px;width:60px"><div style="font-size:4.6px;font-weight:600">option three</div><p class="tiny" style="margin-top:1px">Lorem ipsum dolor sit amet, consectetuer adipiscing elit.</p></div>
  <div class="foot"></div><i class="corner"></i><span class="pg">16</span>
</section>

<!-- 17 Overview chart -->
<section class="slide">
  <i class="slash"></i><i class="slash-lite"></i>
  <h2 class="title">Overview <em>Chart</em></h2>
  <p class="lede">Lorem ipsum dolor sit amet, consectetuer adipiscing elit. Maecenas porttitor congue massa.</p>
  <b class="brand">TIMREL</b>
  <svg class="abs" style="left:10px;top:48px" width="270" height="60" viewBox="0 0 270 60" font-size="3.6" fill="#888" font-family="Poppins,sans-serif">
    <text x="40" y="4" font-size="5">Sales</text><text x="128" y="2" font-size="5">Demand</text><text x="216" y="2" font-size="5">Statistic</text>
    <g stroke="#e4e4e4" stroke-width=".4"><line x1="20" y1="12" x2="90" y2="12"/><line x1="20" y1="22" x2="90" y2="22"/><line x1="20" y1="32" x2="90" y2="32"/><line x1="20" y1="42" x2="90" y2="42"/><line x1="110" y1="10" x2="180" y2="10"/><line x1="110" y1="26" x2="180" y2="26"/><line x1="110" y1="42" x2="180" y2="42"/><line x1="200" y1="10" x2="270" y2="10"/><line x1="200" y1="26" x2="270" y2="26"/><line x1="200" y1="42" x2="270" y2="42"/></g>
    <path d="M20 52V26h20l18 8 17-4 15-8v30z" fill="#6ea6fa"/><path d="M20 52V42h20l18 2 17-10 15-10v28z" fill="#2ec193"/>
    <g fill="#6ea6fa"><rect x="113" y="22" width="6" height="30"/><rect x="129" y="26" width="6" height="26"/><rect x="145" y="22" width="6" height="30"/><rect x="161" y="18" width="6" height="34"/></g>
    <g fill="#203390"><rect x="120" y="30" width="6" height="22"/><rect x="136" y="18" width="6" height="34"/><rect x="152" y="38" width="6" height="14"/><rect x="168" y="30" width="6" height="22"/></g>
    <path d="M212 28c10-16 18-16 28 0s18 10 30-8" fill="none" stroke="#2ec193" stroke-width=".8"/><path d="M212 18c10 0 18 28 30 20s18-14 28-18" fill="none" stroke="#6ea6fa" stroke-width=".8"/>
  </svg>
  <svg class="abs" style="left:27px;top:138px" width="12" height="9"><g fill="#6ea6fa"><rect x="0" y="5" width="2" height="4"/><rect x="3" y="2" width="2" height="7"/><rect x="6" y="4" width="2" height="5"/><rect x="9" y="0" width="2" height="9"/></g></svg>
  <p class="abs tiny" style="left:63px;top:140px;width:200px">It was popularized in the 1960s with the release of sheets containing placeholder passages, and more recently with desktop publishing software including versions of sample text.</p>
  <div class="foot"></div><i class="corner"></i><span class="pg">17</span>
</section>

<!-- 18 World maps -->
<section class="slide">
  <i class="slash"></i><i class="slash-lite"></i>
  <h2 class="title">World <em>Maps</em></h2>
  <p class="lede">Lorem ipsum dolor sit amet, consectetuer adipiscing elit. Maecenas porttitor congue massa.</p>
  <b class="brand">TIMREL</b>
  <div class="abs" role="img" aria-label="World map with North America and China highlighted" style="left:25px;top:55px;width:155px;height:80px;border-radius:30%;background:radial-gradient(ellipse at 30% 45%,#6ea6fa 0 8%,transparent 9%),radial-gradient(ellipse at 68% 48%,#2ec193 0 9%,transparent 10%),linear-gradient(180deg,#e4e5e8,#d6d7da)"></div>
  <div class="abs" style="left:185px;top:54px;width:65px;text-align:center"><div style="font-size:6px;font-weight:600;color:var(--ink)">we are <span style="color:var(--mint)">growing</span></div><p class="tiny" style="margin-top:2px">lorem ipsum dolor sit amet, consectetuer adipiscing elit. maecenas</p></div>
  <div class="abs" style="left:185px;top:104px;width:65px;text-align:center"><div style="font-size:6px;font-weight:600;color:var(--ink)"><span style="color:var(--azure)">join</span> the crew</div><p class="tiny" style="margin-top:2px">lorem ipsum dolor sit amet, consectetuer adipiscing elit. maecenas</p></div>
  <svg class="abs" style="left:211px;top:40px" width="12" height="12"><path d="M2 9h8M6 9V2c-2 2-3 4-4 6" fill="none" stroke="#2ec193" stroke-width=".7"/></svg>
  <svg class="abs" style="left:211px;top:90px" width="12" height="12"><path d="M1 4h7c2 0 2-3 0-3M1 7h9c2 0 2 3 0 3M1 10h5" fill="none" stroke="#517ed8" stroke-width=".7"/></svg>
  <div class="foot"></div><i class="corner"></i><span class="pg">18</span>
</section>

<!-- 19 US maps -->
<section class="slide">
  <i class="slash"></i><i class="slash-lite"></i>
  <h2 class="title">US <em>Maps</em></h2>
  <p class="lede">Lorem ipsum dolor sit amet, consectetuer adipiscing elit. Maecenas porttitor congue massa.</p>
  <b class="brand">TIMREL</b>
  <div class="abs" style="left:23px;top:52px;width:85px"><div style="font-size:4.4px;line-height:1.3">Ut wisi enim ad minim veniam, quis nostrud exerci</div><p class="tiny" style="margin-top:4px;color:#444"><b>Ut wisi enim</b> ad minim veniam, quis nostrud exerci tation ullamcorper nibh euismod tincidunt ut laoreet dolore magna aliquam erat volutpat. Ut wisi enim ad minim veniam, quis nostrud exerci tation ullamcorper nibh euismod tincidunt ut laoreet</p></div>
  <div class="abs" role="img" aria-label="Map of the United States with location pins" style="left:140px;top:56px;width:125px;height:82px;border-radius:18% 25% 30% 20%;background:linear-gradient(180deg,#dedede,#cfcfcf)"></div>
  <svg class="abs" style="left:140px;top:56px" width="125" height="82"><g fill="none" stroke="#333" stroke-width=".7"><path d="M22 18a3 3 0 1 1 6 0c0 2-3 5-3 5s-3-3-3-5z"/><path d="M45 38a3 3 0 1 1 6 0c0 2-3 5-3 5s-3-3-3-5z"/><path d="M90 46a3 3 0 1 1 6 0c0 2-3 5-3 5s-3-3-3-5z"/></g><path d="M54 1a3 3 0 1 1 6 0c0 2-3 5-3 5s-3-3-3-5z" fill="none" stroke="#3758b4" stroke-width=".8" transform="translate(0 6)"/></svg>
  <div class="abs" style="left:186px;top:38px;width:78px;height:13px;background:var(--sky);color:#fff;display:flex;align-items:center;gap:4px;padding-left:5px"><b style="font-size:5.4px;font-weight:600;font-style:italic;color:var(--ink)">70%</b><span style="font-size:2.4px;line-height:1.25">Ut wisi enim ad minim veniam, quis nostrud exerci tation</span></div>
  <div class="foot"></div><i class="corner"></i><span class="pg">19</span>
</section>

<!-- 20 Thank you -->
<section class="slide">
  <svg class="abs" style="left:0;top:0" width="286" height="161"><polygon points="200,0 286,0 286,161 160,161" fill="#060d6c"/></svg>
  <div class="photo" role="img" aria-label="Yacht under sail in deep blue water" style="left:29px;top:27px;width:228px;height:106px;background:linear-gradient(120deg,#203390,#3758b4 50%,#2ec193)"></div>
  <div class="abs" style="left:122px;top:42px;width:44px;height:44px;border-radius:50%;background:radial-gradient(circle,rgba(255,255,255,.18),rgba(255,255,255,0) 70%)"></div>
  <div class="abs" style="left:0;width:286px;top:101px;text-align:center;font-size:10px;font-weight:800;font-style:italic;color:#fff">Thank <span style="color:var(--mint)">You</span></div>
  <p class="abs" style="left:0;width:286px;top:114px;text-align:center;font-size:3.4px;color:#dfe4ff;line-height:1.2">Lorem ipsum is simply dummy text of<br>the printing and typesetting industry.</p>
  <div class="abs" style="left:250px;top:143px;display:flex;gap:1px"><i style="width:6px;height:6px;border:.5px solid var(--sky)"></i><i style="width:6px;height:6px;border:.5px solid var(--sky)"></i><i style="width:6px;height:6px;border:.5px solid var(--sky)"></i><i style="width:6px;height:6px;border:.5px solid var(--sky)"></i></div>
</section>

</main>
</body>
</html>
```